KBMR new business card design

We need a business card design for our established business which is Australia wide however based in Melbourne. We are a young team of Financial Planners who specialize in Insurance and Basic super advice for people like us.

We are people who help our clients get things done in a timely and cost effective manner whilst having a good time and a laugh along the way.

We would like this to have a consistent feel with our new e-brochure which i have attached from a color and font perspective.

Industry/Entity Type

Business

Requirements
Must have
• We do not need specific address details rather just the states we are in:

VIC/NSW/QLD/TAS
Nice to have
• Curved edge to mate the brochure

```html
<!DOCTYPE html>
<html lang="en">
<head>
<meta charset="utf-8">
<title>KBMR Business Card – Back</title>
<link rel="stylesheet" href="https://fonts.googleapis.com/css2?family=Cagliostro&display=swap">
<style>
  :root {
    --page: #ffffff;
    --card: #1d1d1e;
    --card-deep: #141415;
    --green-dark: #07a95a;
    --green-light: #8dc63f;
    --icon-green: #16a955;
    --text-light: #ececec;
    --divider: rgba(255,255,255,0.14);
  }
  * { margin: 0; padding: 0; box-sizing: border-box; }
  html, body {
    width: 1200px; height: 900px; overflow: hidden;
    background: var(--page);
    font-family: "Cagliostro", "Trebuchet MS", sans-serif;
  }
  .card {
    position: absolute; left: 74px; top: 126px;
    width: 1052px; height: 650px;
    background: radial-gradient(ellipse at 50% 45%, var(--card) 0%, var(--card-deep) 100%);
    overflow: hidden;
  }
  .tab {
    position: absolute; left: 0; width: 90px;
  }
  .tab--top {
    top: 180px; height: 146px;
    background: var(--green-dark);
    border-top-right-radius: 30px;
  }
  .tab--bottom {
    top: 326px; height: 144px;
    background: var(--green-light);
    border-bottom-right-radius: 30px;
  }
  .divider {
    position: absolute; left: 522px; top: 50px;
    width: 2px; height: 540px;
    background: linear-gradient(to bottom, transparent, var(--divider) 20%, var(--divider) 80%, transparent);
  }
  .contact { position: absolute; left: 170px; top: 196px; list-style: none; }
  .contact__item {
    display: flex; align-items: center;
    height: 44px; font-size: 26px; color: var(--text-light);
    white-space: nowrap;
  }
  .contact__icon { width: 30px; height: 30px; margin-right: 20px; flex: none; }
  .contact__item--plain { padding-left: 50px; }
  .contact__label { color: var(--green-light); margin-right: 8px; }
  .services { position: absolute; left: 660px; top: 196px; }
  .services__title {
    font-size: 31px; font-weight: 400; color: var(--text-light);
    margin-bottom: 8px; line-height: 44px;
  }
  .services__list { list-style: none; }
  .services__item {
    display: flex; align-items: center;
    height: 39.5px; font-size: 26px; color: var(--green-light);
  }
  .services__item::before {
    content: ""; width: 0; height: 0; margin-right: 10px;
    border-top: 7px solid transparent; border-bottom: 7px solid transparent;
    border-left: 8px solid var(--text-light);
  }
</style>
</head>
<body>
<main class="card" aria-label="KBMR business card">
  <div class="tab tab--top"></div>
  <div class="tab tab--bottom"></div>
  <div class="divider"></div>

  <ul class="contact">
    <li class="contact__item">
      <svg class="contact__icon" viewBox="0 0 30 30" aria-hidden="true">
        <path fill="var(--icon-green)" d="M3 10c0-4 6-6 12-6s12 2 12 6v2h-6v-2c-2-1-10-1-12 0v2H3z"/>
        <path fill="var(--icon-green)" d="M8 14h14l4 12H4z"/>
        <circle cx="15" cy="20" r="3" fill="var(--card)"/>
      </svg>
      <span class="contact__label">Phone:</span>1300 555 104
    </li>
    <li class="contact__item">
      <svg class="contact__icon" viewBox="0 0 30 30" aria-hidden="true">
        <rect x="8" y="3" width="14" height="9" fill="var(--icon-green)"/>
        <rect x="2" y="11" width="26" height="11" rx="2" fill="var(--icon-green)"/>
        <rect x="7" y="19" width="16" height="8" fill="var(--icon-green)" stroke="var(--card)" stroke-width="2"/>
      </svg>
      <span class="contact__label">Fax:</span>03 9555 0182
    </li>
    <li class="contact__item">
      <svg class="contact__icon" viewBox="0 0 30 30" aria-hidden="true">
        <rect x="8" y="2" width="14" height="26" rx="2" fill="var(--icon-green)"/>
        <rect x="10" y="6" width="10" height="16" fill="var(--card)"/>
        <circle cx="15" cy="25" r="1.5" fill="var(--card)"/>
      </svg>
      <span class="contact__label">Mobile:</span>0400 555 287
    </li>
    <li class="contact__item">
      <svg class="contact__icon" viewBox="0 0 30 30" aria-hidden="true">
        <rect x="2" y="6" width="26" height="18" fill="var(--icon-green)"/>
        <path d="M2 7l13 10 13-10" fill="none" stroke="var(--card)" stroke-width="2"/>
      </svg>
      alex@kbmr.com.au
    </li>
    <li class="contact__item">
      <svg class="contact__icon" viewBox="0 0 30 30" aria-hidden="true">
        <rect x="2" y="4" width="26" height="17" rx="1" fill="var(--icon-green)"/>
        <rect x="5" y="7" width="20" height="11" fill="var(--card)"/>
        <rect x="12" y="21" width="6" height="4" fill="var(--icon-green)"/>
        <rect x="8" y="25" width="14" height="2" fill="var(--icon-green)"/>
      </svg>
      www.kbmr.com.au
    </li>
    <li class="contact__item contact__item--plain">NSW,&nbsp; VIC , TAS,&nbsp; QLD</li>
  </ul>

  <section class="services">
    <h2 class="services__title">Specialising in:</h2>
    <ul class="services__list">
      <li class="services__item">Debt Management</li>
      <li class="services__item">Retirement Planning</li>
      <li class="services__item">Risk Insurance</li>
      <li class="services__item">Superannuation</li>
      <li class="services__item">Wealth Creation</li>
    </ul>
  </section>
</main>
</body>
</html>
```